BOLD & MINIMALIST DESIGN NEEDED

We want a very bold but minimalistic business card design that is impactful and utilizes both sides of the business card. Our current logo is included for your use.

We want bold fonts and good use of negative space. We don't want the logo to overpower the design.

Target Market(s)

Professionals who are building new commercial buildings.

Industry/Entity Type

Construction

Contact Information for Business Card

Name, Title, email, office phone, cell phone, website

Font styles to use
Serif
Sans Serif

Requirements
Must have
• Bold design!

```html
<!DOCTYPE html>
<html lang="en">
<head>
<meta charset="utf-8">
<title>Ridgecrest Build Co — Business Card</title>
<link rel="stylesheet" href="https://fonts.googleapis.com/css2?family=Poppins:wght@400;500;600;800&display=swap">
<style>
  :root {
    --bg: #2a2a2a;
    --card-dark: #1f1f1f;
    --card-light: #ffffff;
    --green: #6cc644;
    --ink: #1a1a1a;
    --text-light: #f2f2f2;
  }
  * { box-sizing: border-box; margin: 0; padding: 0; }
  html, body {
    width: 1200px; height: 1195px; overflow: hidden;
    background: var(--bg);
    font-family: "Poppins", sans-serif;
  }
  .stage {
    position: relative; width: 1200px; height: 1195px;
    display: flex; justify-content: center; align-items: center; gap: 60px;
  }
  .card {
    position: relative; width: 400px; height: 640px;
    border-radius: 28px; overflow: hidden;
    box-shadow: 0 20px 40px rgba(0,0,0,.45);
  }
  .card--front { background: var(--card-light); }
  .card--back { background: var(--card-dark); display: flex; align-items: center; justify-content: center; }
  .card__shape { position: absolute; inset: 0; width: 100%; height: 100%; }
  .brand {
    position: absolute; left: 0; right: 0; top: 120px;
    display: flex; align-items: center; justify-content: center; gap: 12px;
  }
  .brand__mark { width: 22px; height: 22px; background: var(--green); }
  .brand__name {
    font-weight: 800; font-size: 34px; letter-spacing: 1px; text-transform: uppercase;
    color: var(--ink); line-height: 1.05; text-align: left;
  }
  .card--back .brand { position: static; }
  .card--back .brand__name { color: var(--card-light); font-size: 40px; }
  .card--back .brand__mark { width: 26px; height: 26px; }
  .contact {
    position: absolute; left: 0; right: 0; top: 390px;
    text-align: center; color: var(--text-light);
  }
  .contact__name { color: var(--green); font-weight: 600; font-size: 26px; line-height: 1.1; }
  .contact__title { font-size: 14px; font-weight: 400; margin-top: 2px; }
  .contact__icons {
    display: flex; align-items: center; justify-content: center; gap: 6px; margin: 14px 0 10px;
  }
  .contact__rule { width: 56px; height: 1px; background: var(--green); margin: 0 10px; }
  .icon { width: 20px; height: 20px; background: var(--green); border-radius: 3px; display: flex; align-items: center; justify-content: center; }
  .icon svg { width: 13px; height: 13px; }
  .contact__lines { font-size: 15px; line-height: 1.45; }
  .contact__divider { width: 40px; height: 1px; background: var(--green); margin: 14px auto; }
  .contact__address { font-size: 14px; line-height: 1.45; }
</style>
</head>
<body>
<main class="stage">
  <section class="card card--front" aria-label="Card front">
    <svg class="card__shape" viewBox="0 0 400 640" preserveAspectRatio="none" aria-hidden="true">
      <path d="M0,300 Q230,250 400,430 L400,640 L0,640 Z" fill="var(--card-dark)"/>
      <path d="M0,272 Q240,228 400,420 Q240,250 0,286 Z" fill="var(--green)"/>
    </svg>
    <div class="brand">
      <span class="brand__mark"></span>
      <span class="brand__name">Ridgecrest<br>Build Co</span>
    </div>
    <div class="contact">
      <p class="contact__name">Daniel Harper</p>
      <p class="contact__title">Head contractor</p>
      <div class="contact__icons">
        <span class="contact__rule"></span>
        <span class="icon"><svg viewBox="0 0 16 16"><path d="M4 2l3 3-2 2c1 2 2 3 4 4l2-2 3 3-2 2C6 14 2 10 2 4z" fill="#fff"/></svg></span>
        <span class="icon"><svg viewBox="0 0 16 16"><rect x="4.5" y="1.5" width="7" height="13" rx="1.5" fill="none" stroke="#fff" stroke-width="1.6"/></svg></span>
        <span class="icon"><svg viewBox="0 0 16 16"><rect x="2" y="4" width="12" height="8" fill="none" stroke="#fff" stroke-width="1.5"/><path d="M2 4l6 5 6-5" fill="none" stroke="#fff" stroke-width="1.5"/></svg></span>
        <span class="icon"><svg viewBox="0 0 16 16"><circle cx="8" cy="8" r="6" fill="none" stroke="#fff" stroke-width="1.5"/><path d="M2 8h12M8 2c-3 3-3 9 0 12M8 2c3 3 3 9 0 12" fill="none" stroke="#fff" stroke-width="1.2"/></svg></span>
        <span class="contact__rule"></span>
      </div>
      <p class="contact__lines">555.014.2200<br>555-014-2201<br>info@ridgecrest.co<br>www.ridgecrest.co</p>
      <div class="contact__divider"></div>
      <p class="contact__address">1420 Stonefield Rd.<br>Cedar Gap, GA 30000</p>
    </div>
  </section>

  <section class="card card--back" aria-label="Card back">
    <div class="brand">
      <span class="brand__mark"></span>
      <span class="brand__name">Ridgecrest<br>Build Co</span>
    </div>
  </section>
</main>
</body>
</html>
```